Business Card Design Project - IT Company

CLOUD IT company working with medium to large corporate clients requires 2 sided Business Card design.

Strong, Professional and modern is what I am looking for.

The Logo JPG attached has all the colour palette options. which consist of Red and Silver on various backgrounds

Preferred option for the Back of card is either Silver Text on Red or Silver Text on Black. Though this is not concrete. Surprise me.

Logo must be prominent along with Contact details of the staff member

Tagline can be all Capitals " CLOUD MANAGED SERVICES"

I will look to provide feedback and tweaks to get the right design so it should be a fun process.

I will provide the layered files to the top few contenders.

Reason: Leaving the door open for some creativity. Don't forget this is an technology company. .

Target Market(s)

Leaders, decision makers, CEOs, CIOs,

Industry/Entity Type

Business

Requirements
Must have
• Data must have is

Company Name: Velquora
Tagline: Cloud Managed Services

No Particular order

First Name Last name
Director
Mobile 0452 987 654
www.velquora.com
First.Lastname@velquora.com
Suite 5, 48 Marlowe Lane, Sydney NSW 2000

```html
<!DOCTYPE html>
<html lang="en">
<head>
<meta charset="utf-8">
<title>Velquora Business Card</title>
<link rel="stylesheet" href="https://fonts.googleapis.com/css2?family=Arimo:wght@400;700&family=Open+Sans:wght@600&display=swap">
<style>
  :root {
    --page-bg: #e9e9e9;
    --card-black: #0b0b0b;
    --card-glow: #222222;
    --silver: #d4d4d4;
    --silver-light: #f2f2f2;
    --grey-text: #8a8a8a;
    --divider: #6a6a6a;
  }
  * { margin: 0; padding: 0; box-sizing: border-box; }
  html, body {
    width: 1200px;
    height: 1200px;
    overflow: hidden;
    background: var(--page-bg);
    font-family: "Arimo", Arial, sans-serif;
  }
  .canvas {
    position: relative;
    width: 1200px;
    height: 1200px;
  }
  .card {
    position: absolute;
    left: 180px;
    width: 840px;
    height: 480px;
    background: radial-gradient(ellipse at 35% 25%, var(--card-glow) 0%, var(--card-black) 65%);
    box-shadow: 0 6px 18px rgba(0,0,0,0.25);
    overflow: hidden;
  }
  .card--front { top: 90px; }
  .card--back { top: 630px; }

  /* Front */
  .title-block {
    position: absolute;
    top: 44px;
    right: 34px;
    text-align: right;
  }
  .title-block__name {
    font-weight: 700;
    font-size: 38px;
    color: var(--silver-light);
    line-height: 1.05;
  }
  .title-block__role {
    font-size: 28px;
    color: var(--grey-text);
    letter-spacing: 0.5px;
    line-height: 1.1;
  }
  .front-mark {
    position: absolute;
    left: 60px;
    top: 350px;
    display: flex;
    align-items: center;
    gap: 10px;
    font-weight: 700;
    font-size: 30px;
    color: var(--silver);
  }
  .front-mark__dot {
    width: 20px;
    height: 20px;
    border-radius: 50%;
    background: var(--silver);
  }
  .divider {
    position: absolute;
    left: 286px;
    top: 290px;
    width: 2px;
    height: 160px;
    background: var(--divider);
  }
  .contact {
    position: absolute;
    left: 322px;
    top: 290px;
    font-size: 22px;
    color: var(--silver-light);
    line-height: 28px;
  }
  .contact__address { margin-top: 18px; }

  /* Back */
  .brand {
    position: absolute;
    right: 110px;
    top: 190px;
    text-align: right;
  }
  .brand__row {
    display: flex;
    align-items: center;
    justify-content: flex-end;
    gap: 22px;
  }
  .brand__dot {
    width: 70px;
    height: 70px;
    border-radius: 50%;
    background: var(--silver);
  }
  .brand__name {
    font-weight: 700;
    font-size: 104px;
    line-height: 1;
    color: var(--silver);
  }
  .brand__tagline {
    font-family: "Open Sans", Arial, sans-serif;
    font-weight: 600;
    font-size: 25px;
    letter-spacing: 0.5px;
    color: var(--silver-light);
    margin-top: 4px;
  }
</style>
</head>
<body>
<main class="canvas">
  <section class="card card--front" aria-label="Card front">
    <div class="title-block">
      <p class="title-block__name">Project Owner</p>
      <p class="title-block__role">DIRECTOR</p>
    </div>
    <div class="front-mark">
      <span class="front-mark__dot"></span>
      <span>Velquora</span>
    </div>
    <div class="divider"></div>
    <div class="contact">
      <p>MOBILE :: (045) 298 7654</p>
      <p>SITE :: www.velquora.com</p>
      <p>E-MAIL :: projectowner@velquora.com</p>
      <div class="contact__address">
        <p>Suite 5, 48 Marlowe Lane,</p>
        <p>Sydney NSW 2000</p>
      </div>
    </div>
  </section>

  <section class="card card--back" aria-label="Card back">
    <div class="brand">
      <div class="brand__row">
        <span class="brand__dot"></span>
        <span class="brand__name">Velquora</span>
      </div>
      <p class="brand__tagline">CLOUD MANAGED SERVICES</p>
    </div>
  </section>
</main>
</body>
</html>
```